Post Card Design - Photo on front, details on back. Logo on both sides.

Back: See the photo of my old card. The back worked well, as it gave me lots of space to write on. The address details are still correct, but the logo has changed to Josephine Sans. Logo can be on one line or on two (if two, align it on the left).
Don't include the 'BEAUTIFUL WEDDING DRESSES...' bit.
I'd like to print this on thicker, slightly coarse paper, so don't go too small on detail.
Here are the Quorl paper details: Paper Stock: Natural Uncoated
Paper Thickness: Premium
Finish: None
Front of Card: I'd like to see options for both pictures:
I think the painted image would look best with a frame in a pale shade and the logo in the frame fairly subtle.
The actual dress photo I'd like to see cropped a bit like in my mock up. You'll need to have a look at how the logo would be best placed on this. You can place it anywhere, or add a banner.
See my website for my brand's look: lorabetwick.co.nz
Target Market(s)
Brides
Industry/Entity Type
Wedding Dresses
Contact Information for Business Card
Front: Photo and logo. Back: with details and lots of empty space. See attached photos for loose brief.
Other font styles liked:
- Josephine Sans
Requirements
Must have
- I hand-write the gown designs and price on the back of the card, so there needs to be plenty of empty space.
Nice to have
- As per brief.
Should not have
- It must look clean, romantic, modern. Timeless.

```html
<!DOCTYPE html>
<html lang="en">
<head>
<meta charset="utf-8">
<title>Lora Betwick – Postcard</title>
<link href="https://fonts.googleapis.com/css2?family=Josefin+Sans:wght@300&family=Mulish:wght@400&display=swap" rel="stylesheet">
<style>
  :root {
    --backdrop: #2e2e2e;
    --cream-frame: #fdf5df;
    --paper-white: #ffffff;
    --ink: #2f2f2f;
    --band-grey: #d9d9d9;
    --photo-light: #f6e8c8;
    --photo-mid: #d9b882;
    --photo-deep: #a7804e;
  }
  * { margin: 0; padding: 0; box-sizing: border-box; }
  html, body {
    width: 1200px; height: 1200px; overflow: hidden;
    background: var(--backdrop);
  }
  .canvas { position: relative; width: 1200px; height: 1200px; }

  .postcard {
    position: absolute;
    box-shadow: 0 6px 14px rgba(0,0,0,0.45);
  }

  /* Front */
  .postcard--front {
    left: 40px; top: 243px; width: 532px; height: 659px;
    background: var(--cream-frame);
  }
  .front-photo {
    position: absolute; left: 17px; top: 17px; right: 17px; bottom: 17px;
    background:
      radial-gradient(ellipse 40% 60% at 72% 55%, rgba(255,250,238,0.85), rgba(255,250,238,0) 70%),
      linear-gradient(100deg, var(--photo-deep) 0%, var(--photo-mid) 30%, var(--photo-light) 60%, var(--photo-mid) 100%);
  }
  .front-wordmark {
    position: absolute; left: 0; right: 0; top: 300px;
    text-align: center; color: var(--ink);
    font-family: "Josefin Sans", sans-serif;
    font-weight: 300; font-size: 43px; letter-spacing: 1.5px; line-height: 1;
  }

  /* Back */
  .postcard--back {
    left: 629px; top: 245px; width: 534px; height: 659px;
    background: var(--paper-white);
  }
  .back-wordmark {
    position: absolute; left: 0; right: 0; top: 22px;
    text-align: center; color: var(--ink);
    font-family: "Josefin Sans", sans-serif;
    font-weight: 300; font-size: 41px; letter-spacing: 1.5px; line-height: 1;
  }
  .contact-band {
    position: absolute; left: 0; right: 0; bottom: 0; height: 76px;
    background: var(--band-grey);
    color: var(--ink);
    font-family: "Mulish", sans-serif; font-weight: 400;
    display: flex; align-items: center; justify-content: center;
  }
  .contact-band__details {
    display: flex; justify-content: center; gap: 11px;
    font-size: 12px; letter-spacing: 1px; line-height: 1;
  }
  .contact-item { display: inline-flex; align-items: center; gap: 3px; }
  .contact-item svg { width: 11px; height: 11px; fill: var(--ink); }
</style>
</head>
<body>
<div class="canvas">

  <section class="postcard postcard--front">
    <div class="front-photo" role="img" aria-label="Photograph of a bride in an off-shoulder satin gown with a long train, standing in a sunlit stone colonnade"></div>
    <div class="front-wordmark">LORA BETWICK</div>
  </section>

  <section class="postcard postcard--back">
    <div class="back-wordmark">LORA BETWICK</div>
    <div class="contact-band">
      <div class="contact-band__details">
        <span class="contact-item">
          <svg viewBox="0 0 24 24" aria-hidden="true"><path d="M6.6 10.8a15.1 15.1 0 0 0 6.6 6.6l2.2-2.2a1 1 0 0 1 1-.25 11.4 11.4 0 0 0 3.6.57 1 1 0 0 1 1 1V20a1 1 0 0 1-1 1A17 17 0 0 1 3 4a1 1 0 0 1 1-1h3.5a1 1 0 0 1 1 1c0 1.25.2 2.45.57 3.570a1 1 0 0 1-.25 1z"/></svg>
          +64 9 555 0147
        </span>
        <span class="contact-item">
          <svg viewBox="0 0 24 24" aria-hidden="true"><path d="M2 5h20v14H2z M4 7v.4l8 5.2 8-5.2V7z" fill-rule="evenodd"/></svg>
          lora@lorabetwick.co.nz
        </span>
        <span class="contact-item">
          <svg viewBox="0 0 24 24" aria-hidden="true"><path d="M12 2a10 10 0 1 0 0 20 10 10 0 0 0 0-20zm0 2c.9 1.2 1.6 2.7 1.9 4h-3.8c.3-1.3 1-2.8 1.9-4zM4.3 14a8 8 0 0 1 0-4h3.4a16 16 0 0 0 0 4zm.9 2h3c.3 1.3.8 2.5 1.4 3.6A8 8 0 0 1 5.2 16zm3-8h-3a8 8 0 0 1 4.4-3.6C8.9 5.5 8.5 6.7 8.2 8zM12 20c-.9-1.2-1.6-2.7-1.9-4h3.8c-.3 1.3-1 2.8-1.9 4zm2.3-6H9.7a14 14 0 0 1 0-4h4.6a14 14 0 0 1 0 4zm.1 5.6c.6-1.1 1.1-2.3 1.4-3.6h3a8 8 0 0 1-4.4 3.6zM16.3 14a16 16 0 0 0 0-4h3.4a8 8 0 0 1 0 4zm-.5-6c-.3-1.3-.8-2.5-1.4-3.6A8 8 0 0 1 18.8 8z"/></svg>
          lorabetwick.co.nz
        </span>
      </div>
    </div>
  </section>

</div>
</body>
</html>
```